KRV Construction Management -Business card design request- Lioness black and white shema ONLY - No

It is a woman on construction company I would like the schema to be in black-and-white with the lioness and possibly a lion anulinus as me and my husband both kind of running I would like to see designs for both. Original art would be preferred but like I said I'm going to attach some pictures that I really like and also if you could check my website out that would be great.Please get very creative this is a very important company I will be combining quality construction services with quality construction company and community affiliates such as Halvick construction exedra I really need to show dominates all I'm really wanting is the black-and-white montre and the lioness image on the right side as you will see in some of the thumbnails from what I have had in the past it is OK but I can't connect with anything. These are the last of my advertising dollars I ask that you really please put some time and help me take my company it to the next century. This is going to be a global thing it will be very serious. I'm not trying to be arrogant I'm just trying to tell the truth I ask that you give me something of quality that something that I can put on folders billboards pains walking to places and that it's not that I'm a woman own business but I deftly want there to be A-line as and please play around with the image of the lion and lioness as my husband is a lot of the construction side and I have a decided if Im going to advertise that are notJmsconstructionmanagement.comJovanna Schlossenberg C.E.O.KRV Construction Management Marisela@jmsconstructionmanagement.com81.316.0990

Target Market(s)

Construction or management style. Understand theme ports of marketing and that this logo will be displayed on billboards D cows apps all across the country

Industry/Entity Type

Construction Company

Contact Information for Business Card

Marisela Vandertook
C.E.O.

Marisela@krvconstructionmanagement.example

Www.krvconstructionmanagement.example

729.584.1437

If you can I would like my slogan on their connecting qualify construction services with qualified construction companies and community affiliates

Font styles to use
Sans Serif

Colors
ffffff

Requirements
Must have
• Black-and-white schema lioness on the back side I will list my services will get to that but for now I wanna get the logo design I very open to where you maneuver the contact information
• Marisela Vandertook
• C.E.O.
• Marisela@krvconstructionmanagement.example
• Www.krvconstructionmanagement.example
• 729.584.1437
• If you can I would like my slogan on their connecting qualified construction services with qualified construction companies and community affiliates
Nice to have
• Everything I mentioned above.
• I have added a few pictures with a lion and Linus and know this may seem crazy but I do not like that they are facing to the left I would rather the lion and lioness looked to the right and face forward. Also all the images need to be in black-and-white have provided some color want but I'd like them change to sepia .
Should not have
• I do not want it to look like a cartoon I need this to be of the utmost professionalism

```html
<!DOCTYPE html>
<html lang="en">
<head>
<meta charset="utf-8">
<title>KRV Construction Management – Business Card</title>
<link rel="stylesheet" href="https://fonts.googleapis.com/css2?family=Roboto:wght@500;700&family=Raleway:wght@400&display=swap">
<style>
  :root {
    --page: #ececec;
    --ink: #050505;
    --paper: #ffffff;
    --panel-grey: #c3c3c5;
    --photo-dark: #1e1e1e;
    --photo-mid: #6a6a6a;
    --photo-light: #9a9a9a;
  }
  * { margin: 0; padding: 0; box-sizing: border-box; }
  html, body {
    width: 1200px;
    height: 1192px;
    overflow: hidden;
    background: var(--page);
  }
  .sheet { position: relative; width: 1200px; height: 1192px; }

  .card {
    position: absolute;
    left: 190px;
    width: 820px;
    height: 561px;
    overflow: hidden;
    background: var(--ink);
  }
  .card--front { top: 20px; }
  .card--back { top: 611px; }

  /* Front */
  .brand-panel {
    position: absolute;
    left: 0; top: 0;
    width: 388px; height: 100%;
    background: var(--ink);
    color: var(--paper);
    font-family: "Roboto", Arial, sans-serif;
    font-weight: 700;
  }
  .brand-mark {
    position: absolute;
    left: 52px;
    top: 160px;
    font-size: 146px;
    line-height: 1;
    letter-spacing: -2px;
  }
  .brand-sub {
    position: absolute;
    left: 0;
    width: 100%;
    top: 296px;
    text-align: center;
    font-size: 46px;
    line-height: 52px;
    letter-spacing: -0.5px;
  }
  .photo-area {
    position: absolute;
    left: 388px; top: 0;
    width: 432px; height: 100%;
    background:
      radial-gradient(ellipse 70% 55% at 72% 45%, var(--photo-light) 0%, var(--photo-mid) 45%, transparent 80%),
      linear-gradient(100deg, var(--photo-dark) 0%, #3a3a3a 40%, var(--photo-mid) 100%);
  }

  /* Back */
  .back-header {
    position: absolute;
    left: 0; top: 0;
    width: 100%; height: 272px;
    background: var(--ink);
    color: var(--paper);
    text-align: center;
  }
  .slogan {
    position: absolute;
    left: 0; width: 100%;
    top: 76px;
    font-family: "Raleway", Arial, sans-serif;
    font-size: 17px;
    line-height: 22px;
    letter-spacing: 1.6px;
    color: #e6e6e6;
  }
  .holder-name {
    position: absolute;
    left: 0; width: 100%;
    top: 218px;
    font-family: "Roboto", Arial, sans-serif;
    font-weight: 700;
    font-size: 33px;
    letter-spacing: 3.4px;
  }
  .contact-panel {
    position: absolute;
    left: 0; top: 272px;
    width: 100%; height: 289px;
    background: var(--panel-grey);
  }
  .contact-list { list-style: none; }
  .contact-item {
    position: absolute;
    left: 108px;
    display: flex;
    align-items: center;
    gap: 12px;
    font-family: "Roboto", Arial, sans-serif;
    font-weight: 500;
    font-size: 20px;
    letter-spacing: 2.2px;
    color: var(--ink);
  }
  .contact-item:nth-child(1) { top: 52px; }
  .contact-item:nth-child(2) { top: 110px; }
  .contact-item:nth-child(3) { top: 167px; }
  .contact-icon { width: 39px; height: 39px; flex: none; }
</style>
</head>
<body>
<main class="sheet">

  <section class="card card--front" aria-label="Business card front">
    <div class="brand-panel">
      <div class="brand-mark">KRV</div>
      <div class="brand-sub">Construction<br>Management</div>
    </div>
    <div class="photo-area" role="img" aria-label="Black and white close-up photograph of a lioness looking forward"></div>
  </section>

  <section class="card card--back" aria-label="Business card back">
    <header class="back-header">
      <p class="slogan">Connecting qualified construction services would qualify<br>construction companies and community affiliates</p>
      <h1 class="holder-name">Marisela Vandertook(C.E.O.)</h1>
    </header>
    <div class="contact-panel">
      <ul class="contact-list">
        <li class="contact-item">
          <svg class="contact-icon" viewBox="0 0 40 40" aria-hidden="true">
            <circle cx="20" cy="20" r="20" fill="#050505"/>
            <rect x="11" y="13.5" width="18" height="13" fill="none" stroke="#fff" stroke-width="1.8"/>
            <path d="M11 13.5 L20 21 L29 13.5 M11 26.5 L17.5 19 M29 26.5 L22.5 19" fill="none" stroke="#fff" stroke-width="1.8"/>
          </svg>
          <span>Marisela@krvconstructionmanagement.example</span>
        </li>
        <li class="contact-item">
          <svg class="contact-icon" viewBox="0 0 40 40" aria-hidden="true">
            <circle cx="20" cy="20" r="20" fill="#050505"/>
            <path d="M14 12 l4 4 -2.5 2.5 c1.2 2.6 3.4 4.8 6 6 L24 22 l4 4 -2.6 2.6 C18 28 12 22 11.4 14.6 Z" fill="#fff"/>
          </svg>
          <span>www.krvconstructionmanagement.example</span>
        </li>
        <li class="contact-item">
          <svg class="contact-icon" viewBox="0 0 40 40" aria-hidden="true">
            <circle cx="20" cy="20" r="20" fill="#050505"/>
            <g fill="none" stroke="#fff" stroke-width="1.5">
              <circle cx="20" cy="20" r="10"/>
              <ellipse cx="20" cy="20" rx="4.5" ry="10"/>
              <path d="M10 20 H30 M12 14.5 H28 M12 25.5 H28"/>
            </g>
          </svg>
          <span>729.584.1437</span>
        </li>
      </ul>
    </div>
  </section>

</main>
</body>
</html>
```